United States DNA testing company needs full set of banner ads

Nationwide DNA testing services company needs a set of banner ads that I can use in Google Adwords display ads. We also want to be able to use one of them on our website. Therefore, we need all of the sizes Adwords uses (Vertical rectangle: 240 x 400, Mobile leaderboard: 320 x 50, Banner: 468 x 60, Leaderboard: 728 x 90, Square: 250 x 250, Small square: 200 x 200, Large rectangle: 336 x 280, Inline rectangle: 300 x 250, Skyscraper: 120 x 600). Please keep our website colors and look and feel in mind. My website is kelvroth.com. Although some will be driving visitors to our home page our goal is to drive them to use our "Lineage Lantern", which is a new element designed to drive visitors to (in just 3 simple steps) pick the right DNA paternity test for their specific situation. Caucasian men, 20-29 are our target market, but often times female's do all the research and share info with men. The steps involved in the Lineage Lantern are as follows: Step 1- Select the relationship that best describes them, e.g. Alleged Father, Mother, Child. Step 2- Why do you need the test, e.g. Child Support, Child Custody, etc. Step 3- What city do you live in? The element then returns a page with the recommended test, the correct number to call and with language directed to the visitor's relationship status, e.g. Alleged Father, Mother, child. The element has been created to drive calls in our call center. We serve private individuals throughout the US. I have attached an ai version of our logo, but will be happy to upload other images from our site, if you need them. Last thing, please use some type of motion with these ads. Thanks!

Industry/Entity Type

It Company

```html
<!DOCTYPE html>
<html lang="en">
<head>
<meta charset="utf-8">
<title>Kelvroth DNA Labs – Banner Set</title>
<link rel="stylesheet" href="https://fonts.googleapis.com/css2?family=Bitter:wght@700&family=Noto+Serif&family=PT+Sans:wght@400;700&family=Sorts+Mill+Goudy&display=swap">
<style>
  :root{
    --wood-1:#e2bf8f;
    --wood-2:#d4ab74;
    --wood-3:#e8c89c;
    --slot:rgba(238,226,208,.42);
    --slot-edge:rgba(255,255,255,.35);
    --red:#c8202a;
    --red-dark:#a8151d;
    --navy:#353d5e;
    --ink:#4a4a4a;
    --label-dark:#1d1a16;
    --white:#ffffff;
    --photo-a:#c9b6a4;
    --photo-b:#5a7fb8;
  }
  *{box-sizing:border-box;margin:0;padding:0}
  html,body{width:1200px;height:1200px;overflow:hidden}
  body{
    position:relative;
    background:linear-gradient(90deg,var(--wood-1) 0%,var(--wood-3) 18%,var(--wood-2) 36%,var(--wood-3) 55%,var(--wood-1) 74%,var(--wood-2) 100%);
    font-family:"Noto Serif",serif;
  }
  .slot{
    position:absolute;background:var(--slot);
    box-shadow:0 0 0 1px var(--slot-edge),1px 2px 4px rgba(0,0,0,.15);
    display:flex;align-items:center;justify-content:center;
    color:var(--white);font-family:"Sorts Mill Goudy",serif;font-size:32px;letter-spacing:1px;
  }
  .size-label{position:absolute;font-family:"Sorts Mill Goudy",serif;color:var(--label-dark);font-size:28px;text-align:center;line-height:25px}
  .banner{position:absolute;background:var(--white);overflow:hidden;box-shadow:1px 2px 5px rgba(0,0,0,.3)}
  .banner svg.shape{position:absolute;left:0;top:0}
  .brand{position:absolute;display:flex;align-items:center;gap:6px;color:var(--navy);font-family:"Bitter",serif;font-weight:700;line-height:1}
  .brand-dot{border-radius:50%;background:var(--red);flex:none}
  .tagline{position:absolute;font-family:"PT Sans",sans-serif;font-weight:700;font-style:italic;color:var(--navy)}
  .headline{position:absolute;font-family:"Bitter",serif;font-weight:700;color:var(--red);line-height:1.1}
  .body-copy{position:absolute;color:var(--ink);line-height:1.2}
  .photo{position:absolute;background:linear-gradient(160deg,var(--photo-a) 0%,#e9ddd2 45%,var(--photo-b) 100%)}
  .cta{
    position:absolute;background:linear-gradient(var(--red),var(--red-dark));color:var(--white);
    font-family:"PT Sans",sans-serif;border-radius:3px;text-align:center;
    box-shadow:0 0 0 1px rgba(255,255,255,.5),0 2px 3px rgba(0,0,0,.35);line-height:1
  }
  .cta small{display:block;font-size:12px}
  .cta strong{display:block;font-size:25px;font-weight:700}
</style>
</head>
<body>

  <!-- empty size slots -->
  <div class="slot" style="left:153px;top:78px;width:240px;height:400px">240 x 400</div>
  <div class="slot" style="left:566px;top:320px;width:200px;height:200px">200 x 200</div>
  <div class="slot" style="left:566px;top:546px;width:250px;height:250px">250 x 250</div>
  <div class="slot" style="left:566px;top:825px;width:320px;height:50px">320 x 50</div>
  <div class="slot" style="left:564px;top:897px;width:468px;height:60px">468 x 60</div>
  <div class="slot" style="left:57px;top:779px;width:336px;height:280px">336 x 280</div>

  <div class="size-label" style="left:440px;top:272px;width:70px">120<br>x<br>600</div>
  <div class="size-label" style="left:-12px;top:613px;width:150px;transform:rotate(-90deg)">300 x 250</div>
  <div class="size-label" style="left:700px;top:1070px;width:160px">729 x 90</div>

  <!-- inline rectangle 300 x 250 -->
  <div class="banner inline-rect" style="left:93px;top:502px;width:300px;height:250px">
    <div class="photo" role="img" aria-label="Smiling father carrying his young son on his back" style="left:110px;top:92px;width:180px;height:110px"></div>
    <svg class="shape" width="300" height="250" viewBox="0 0 300 250">
      <path d="M0 200 Q150 195 300 168 L300 250 L0 250Z" fill="var(--red)"/>
      <path d="M0 205 Q150 200 300 176 L300 250 L0 250Z" fill="var(--navy)"/>
    </svg>
    <div class="brand" style="left:20px;top:22px;font-size:27px"><span class="brand-dot" style="width:16px;height:16px"></span>Kelvroth DNA Labs</div>
    <div class="tagline" style="left:68px;top:74px;font-size:10px">Seeking the truth when it matters most</div>
    <div class="headline" style="left:8px;top:101px;font-size:22px">Lineage Lantern</div>
    <div class="body-copy" style="left:9px;top:135px;font-size:15px;line-height:17px">Pick the right<br>DNA paternity<br>test for you</div>
    <div class="cta" style="left:70px;top:213px;width:165px;height:28px;font-size:15px;padding-top:6px">Click here to Begin</div>
  </div>

  <!-- skyscraper 120 x 600 -->
  <div class="banner skyscraper" style="left:417px;top:358px;width:120px;height:600px">
    <div class="photo" role="img" aria-label="Smiling father carrying his young son on his back" style="left:0;top:270px;width:120px;height:210px"></div>
    <svg class="shape" width="120" height="600" viewBox="0 0 120 600">
      <path d="M0 470 Q60 472 120 458 L120 600 L0 600Z" fill="var(--red)"/>
      <path d="M0 477 Q60 478 120 466 L120 600 L0 600Z" fill="var(--navy)"/>
    </svg>
    <div class="brand" style="left:6px;top:22px;width:110px;font-size:20px;flex-wrap:wrap;text-align:center;justify-content:center">Kelvroth<br>DNA Labs</div>
    <div class="tagline" style="left:4px;top:84px;font-size:6px">Seeking the truth when it matters most</div>
    <div class="headline" style="left:0;top:130px;width:120px;text-align:center;font-size:22px">Lineage<br>Lantern</div>
    <div class="body-copy" style="left:0;top:197px;width:120px;text-align:center;font-size:14px;line-height:19px">pick the right<br>DNA paternity<br>test for you</div>
    <div class="cta" style="left:10px;top:518px;width:100px;height:48px;padding-top:6px"><small>Click here to</small><strong>BEGIN</strong></div>
  </div>

  <!-- leaderboard 728 x 90 -->
  <div class="banner leaderboard" style="left:418px;top:969px;width:728px;height:90px">
    <div class="photo" role="img" aria-label="Smiling father carrying his young son on his back" style="left:194px;top:0;width:166px;height:90px"></div>
    <svg class="shape" width="728" height="90" viewBox="0 0 728 90">
      <path d="M570 0 L728 0 L728 90 L572 90 Q582 45 570 0Z" fill="var(--red)"/>
      <path d="M580 0 L728 0 L728 90 L582 90 Q592 45 580 0Z" fill="var(--navy)"/>
    </svg>
    <div class="brand" style="left:10px;top:24px;font-size:22px"><span class="brand-dot" style="width:14px;height:14px"></span>Kelvroth DNA Labs</div>
    <div class="tagline" style="left:42px;top:63px;font-size:8px">Seeking the truth when it matters most</div>
    <div class="headline" style="left:366px;top:14px;font-size:24px">Lineage Lantern</div>
    <div class="body-copy" style="left:360px;top:42px;width:200px;text-align:center;font-size:14px;line-height:19px">pick the right DNA paternity<br>test for you</div>
    <div class="cta" style="left:610px;top:22px;width:99px;height:49px;padding-top:7px"><small>Click here to</small><strong>BEGIN</strong></div>
  </div>

</body>
</html>
```